Flyer Design

Company name Brightgrate, ecofriendly oven cleaning. See website brightgrate.co.uk. Looking for a flyer to offer a 10% discount off web prices Picture of shiny oven, highlighting eco aspect

Industry/Entity Type

It Company

```html
<!DOCTYPE html>
<html lang="en">
<head>
<meta charset="utf-8">
<title>Brightgrate Flyer</title>
<link href="https://fonts.googleapis.com/css2?family=Open+Sans:ital,wght@0,400;0,600;0,700;0,800;1,400;1,600;1,700&display=swap" rel="stylesheet">
<style>
  :root {
    --stage: #9dbdca;
    --stage-deep: #6f98aa;
    --paper: #ffffff;
    --frame: #d3d5d6;
    --ink: #1d1d1d;
    --green: #9fd45a;
    --green-deep: #7dbb2c;
    --dark-1: #2d2d2d;
    --dark-2: #6a6a6a;
  }
  * { box-sizing: border-box; margin: 0; padding: 0; }
  html, body { width: 1200px; height: 1037px; overflow: hidden; }
  body {
    font-family: "Open Sans", Arial, sans-serif;
    background: radial-gradient(ellipse at 50% 55%, #d5e6ec 0%, var(--stage) 45%, var(--stage-deep) 100%);
    position: relative;
  }
  .flyer {
    position: absolute; left: 60px; top: 138px;
    width: 1080px; height: 760px;
    background: var(--frame);
    box-shadow: 0 30px 60px rgba(40,70,85,.35);
    overflow: hidden;
  }
  .hero {
    position: absolute; left: 0; top: 0; width: 1080px; height: 300px;
    background: linear-gradient(100deg, var(--dark-1) 0%, #4a4a4a 40%, var(--dark-2) 75%, #8a8a8a 100%);
  }
  .brand-panel {
    position: absolute; left: 0; top: 22px; width: 420px; height: 96px;
    background: var(--paper);
    clip-path: polygon(0 0, 100% 0, 96% 100%, 0 100%);
    padding: 12px 0 0 28px;
  }
  .brand-name {
    font-size: 46px; font-weight: 700; color: var(--green-deep);
    line-height: 1.05;
  }
  .brand-tag {
    font-size: 13px; font-style: italic; font-weight: 600; color: var(--green-deep);
    margin-top: 4px; padding-left: 2px;
  }
  .call-panel {
    position: absolute; left: 440px; top: 18px; width: 440px; height: 88px;
    background: var(--paper);
    clip-path: polygon(3% 0, 100% 0, 97% 100%, 0 100%);
    display: flex; align-items: center; gap: 26px; padding-left: 38px;
  }
  .call-label { font-size: 24px; font-weight: 700; color: var(--ink); }
  .call-number { font-size: 38px; font-weight: 800; color: var(--ink); letter-spacing: 1px; }
  .discount {
    position: absolute; left: 870px; top: 0; width: 210px; height: 190px;
    background: linear-gradient(150deg, rgba(255,255,255,.95) 0%, rgba(255,255,255,.85) 60%, rgba(255,255,255,0) 61%);
    padding: 22px 0 0 70px;
  }
  .discount-text {
    font-size: 34px; font-weight: 700; color: var(--green);
    line-height: 1.05; text-align: center; width: 90px;
  }
  .intro {
    position: absolute; left: 26px; top: 134px; width: 620px; color: #f2f2f2;
  }
  .intro h2 {
    font-size: 18px; font-weight: 700; font-style: italic; color: var(--green);
    margin-bottom: 4px;
  }
  .intro h3 {
    font-size: 16px; font-weight: 700; font-style: italic; color: var(--green);
    margin: 8px 0 3px;
  }
  .intro p { font-size: 13px; font-style: italic; line-height: 1.5; letter-spacing: .4px; }
  .price-grid {
    position: absolute; left: 14px; top: 314px; width: 1052px; height: 432px;
    display: grid; grid-template-columns: repeat(3, 1fr); grid-template-rows: repeat(2, 1fr);
    gap: 14px;
  }
  .price-card {
    background: var(--paper);
    display: flex; padding: 18px 18px; gap: 14px;
  }
  .price-card .product {
    flex: 0 0 96px; height: 96px; border-radius: 3px;
  }
  .product.steel { background: linear-gradient(135deg, #f2f2f2, #9ea3a6 60%, #d6d8d9); }
  .product.range { background: linear-gradient(135deg, #e6e8e9, #8d9296 55%, #c9cccd); }
  .product.hob { background: linear-gradient(135deg, #c7c9ca, #6c7073 60%, #a9acae); }
  .product.cooker { background: linear-gradient(135deg, #3f7a58, #1f4c33 65%, #2d5f42); }
  .product.hood { background: linear-gradient(180deg, #fafafa, #cfd2d4 70%, #e4e6e7); }
  .card-body { flex: 1; min-width: 0; }
  .card-title {
    font-size: 15.5px; font-weight: 700; color: var(--green);
    margin-bottom: 12px; white-space: nowrap;
  }
  .price-list { list-style: none; font-size: 14px; font-style: italic; color: var(--ink); line-height: 1.5; }
  .price-list li { display: flex; justify-content: flex-end; gap: 8px; }
  .price-list .price { color: var(--green); width: 42px; text-align: left; }
  .price-list .note { font-size: 11px; line-height: 1.25; text-align: right; padding-right: 50px; }
</style>
</head>
<body>
  <main class="flyer">
    <section class="hero" role="img" aria-label="Black and white photo of a clean modern kitchen">
      <div class="brand-panel">
        <div class="brand-name">Brightgrate</div>
        <div class="brand-tag">natural oven care specialists</div>
      </div>
      <div class="call-panel">
        <span class="call-label">Call us</span>
        <span class="call-number">07700 900318</span>
      </div>
      <div class="discount">
        <div class="discount-text">DISC<br>10%</div>
      </div>
      <div class="intro">
        <h2>Your local professional oven cleaning company</h2>
        <p>We are a family run business providing an outstanding and professional oven cleaning service in Harlow Bay, Westcombe and the surrounding villages.</p>
        <h3>How we clean</h3>
        <p>We clean ovens to the highest possible standards. All the removable parts of the appliance will be carefully taken out and placed in our van-mounted tank.</p>
      </div>
    </section>

    <section class="price-grid">
      <article class="price-card">
        <div class="product steel" role="img" aria-label="Photo of a stainless built-in double oven"></div>
        <div class="card-body">
          <h4 class="card-title">Standard Ovens – 60cm</h4>
          <ul class="price-list">
            <li>Single <span class="price">£45</span></li>
            <li>1 1/2 Oven/Grill <span class="price">£55</span></li>
            <li>Electric Hob - add <span class="price">£13</span></li>
            <li>Gas Hob - add <span class="price">£15</span></li>
          </ul>
        </div>
      </article>
      <article class="price-card">
        <div class="product range" role="img" aria-label="Photo of a large stainless range oven"></div>
        <div class="card-body">
          <h4 class="card-title">Large Range Ovens–110cm</h4>
          <ul class="price-list">
            <li>2 Oven <span class="price">£65</span></li>
            <li>3 Oven <span class="price">£80</span></li>
            <li>4 Oven <span class="price">£90</span></li>
            <li>Including Hob + <span class="price">£20</span></li>
          </ul>
        </div>
      </article>
      <article class="price-card">
        <div class="product range" role="img" aria-label="Photo of a small stainless range oven"></div>
        <div class="card-body">
          <h4 class="card-title">Small Range Ovens - 90cm</h4>
          <ul class="price-list">
            <li>Oven <span class="price">£55</span></li>
            <li>Including Hob <span class="price">£70</span></li>
          </ul>
        </div>
      </article>
      <article class="price-card">
        <div class="product hob" role="img" aria-label="Photo of a gas hob"></div>
        <div class="card-body">
          <h4 class="card-title">Hobs</h4>
          <ul class="price-list">
            <li>4 Ring Electric <span class="price">£13</span></li>
            <li>4 Ring Gas <span class="price">£15</span></li>
            <li>5 Ring <span class="price">£20</span></li>
            <li>6-8 Ring <span class="price">£25</span></li>
          </ul>
        </div>
      </article>
      <article class="price-card">
        <div class="product cooker" role="img" aria-label="Photo of a green heat-storage range cooker"></div>
        <div class="card-body">
          <h4 class="card-title">Heat-Storage Cookers</h4>
          <ul class="price-list">
            <li>2 Oven <span class="price">£70</span></li>
            <li>3 Oven <span class="price">£90</span></li>
            <li>4 Oven <span class="price">£110</span></li>
          </ul>
        </div>
      </article>
      <article class="price-card">
        <div class="product hood" role="img" aria-label="Photo of a stainless extraction hood"></div>
        <div class="card-body">
          <h4 class="card-title">Other Appliances</h4>
          <ul class="price-list">
            <li>Extraction Hood <span class="price">£20</span></li>
            <li class="note">(Including free filter replacement where necessary)</li>
            <li>Microwave <span class="price">£18</span></li>
            <li>BBQ <span class="price">£45</span></li>
          </ul>
        </div>
      </article>
    </section>
  </main>
</body>
</html>
```